new Tavrin Care flyer

Redesign our flyer completely. A copy of our current flyers are attached (which are being combined into 1). Use anything from these that u want.
It's given to patients with a whole lot of flyers from our competitors - so needs to stand out
Essential elements are:
1. Text: $99 CPAP Trial (prominent - this is the main point of the flyer)
- Our all inclusive 4 week CPAP or APAP trial includes everything you need to get started for just $99. Plus we'll refund your trial fee when you're ready to buy your own machine.
2. Text: Proudly Independent! (keep this separate from themain promotion.
- Many CPAP clinics in Victoria are now owned by one or other of the big CPAP manufacturers; while many others only stock one brand. We stock all the leading brands and offer genuinely independent advice and friendly service.
3. Text: Call us for an appointment
- Ashburton (03) 9412 6083 5/418 Dorran Street (suburb and phone prominent)
- Brighton (03) 9263 5540 27b Tamsley Grove (suburb and phone prominent)
- Kew East (03) 9351 2874 2637 Fennick Road (suburb and phone prominent)
4. Our logo - attached
5. small supplier logos grouped together - corvane, talvix, morrow&dunlee - attached
6. images for background / filler - talvix machine, mdh machine - attached, must use at least one of talvix pics

```html
<!DOCTYPE html>
<html lang="en">
<head>
<meta charset="utf-8">
<title>Tavrin Care – $99 CPAP Trial Flyer</title>
<link href="https://fonts.googleapis.com/css2?family=Bebas+Neue&family=Open+Sans:wght@600;700;800&family=Arimo:wght@400;700&display=swap" rel="stylesheet">
<style>
  :root {
    --page-bg: #e6e6e6;
    --paper: #ffffff;
    --paper-shade: #ececec;
    --green: #6cb52d;
    --green-dark: #3f9a2a;
    --green-light: #8cc63f;
    --blue: #1aa3d3;
    --blue-dark: #0c6f9c;
    --navy: #0e2436;
    --ink: #1c1c1c;
    --machine-dark: #2a2d31;
    --machine-mid: #5b6066;
  }
  * { box-sizing: border-box; margin: 0; padding: 0; }
  html, body { width: 900px; height: 1200px; overflow: hidden; background: var(--page-bg); }
  .canvas { position: relative; width: 900px; height: 1200px; }
  .flyer {
    position: absolute; left: 167px; top: 17px;
    width: 566px; height: 1165px;
    background: linear-gradient(180deg, var(--paper) 0%, var(--paper) 55%, var(--paper-shade) 85%);
    overflow: hidden;
    box-shadow: 0 4px 18px rgba(0,0,0,.18);
  }
  .flyer-shapes { position: absolute; inset: 0; }
  .brand-name {
    position: absolute; left: 0; right: 0; top: 48px;
    text-align: center;
    font-family: "Open Sans", sans-serif; font-weight: 700;
    font-size: 66px; letter-spacing: 1px; line-height: 1;
    color: var(--green);
  }
  .hero-machine {
    position: absolute; left: 67px; top: 150px; width: 437px; height: 240px;
    border-radius: 22px;
    background: linear-gradient(90deg, var(--machine-dark) 0%, var(--machine-mid) 62%, #d7dce0 72%, #eef1f3 100%);
  }
  .about { position: absolute; left: 35px; top: 518px; width: 275px; }
  .about-title {
    font-family: "Open Sans", sans-serif; font-weight: 800;
    font-size: 31px; color: var(--green-dark); line-height: 1;
  }
  .about-tagline {
    margin-top: 8px;
    font-family: "Open Sans", sans-serif; font-weight: 700;
    font-size: 20px; line-height: 1.1; color: var(--blue-dark);
  }
  .about-body {
    margin-top: 12px;
    font-family: "Arimo", sans-serif; font-size: 18.5px; line-height: 24px;
    color: var(--ink);
  }
  .trial-offer {
    position: absolute; left: 326px; top: 484px; width: 210px; height: 362px;
    text-align: center; font-family: "Bebas Neue", sans-serif; line-height: .92;
  }
  .trial-price { margin-top: 26px; font-size: 96px; color: var(--ink); }
  .trial-label { font-size: 70px; color: var(--paper); }
  .trial-details {
    margin: 8px 14px 0;
    font-family: "Open Sans", sans-serif; font-weight: 600;
    font-size: 12px; line-height: 14.5px; color: var(--paper);
  }
  .refund-note {
    position: absolute; left: 0; top: 862px; width: 300px; height: 140px;
    border-radius: 0 26px 26px 0;
    background: linear-gradient(180deg, #3ab8e2 0%, var(--blue) 45%, var(--blue-dark) 100%);
    font-family: "Open Sans", sans-serif; font-weight: 700;
    padding: 12px 0 0 60px; line-height: 1.02;
  }
  .refund-lead { font-size: 24px; color: var(--navy); }
  .refund-main { font-size: 32px; color: var(--navy); }
  .refund-tail { font-size: 22px; color: var(--paper); }
  .machine-inset {
    position: absolute; left: 352px; top: 862px; width: 172px; height: 172px;
    border-radius: 50%; border: 6px solid var(--paper);
    background: radial-gradient(circle at 45% 55%, #3c4046 0%, #24272b 45%, #8f8a84 100%);
    box-shadow: 0 3px 8px rgba(0,0,0,.25);
  }
  .contact { position: absolute; left: 22px; top: 1058px; width: 522px; color: var(--paper); }
  .contact-title {
    font-family: "Open Sans", sans-serif; font-weight: 800;
    font-size: 15px; line-height: 1; text-transform: uppercase; letter-spacing: .5px;
  }
  .clinics { display: flex; justify-content: space-between; margin-top: 8px; }
  .clinic { width: 168px; font-family: "Open Sans", sans-serif; }
  .clinic-suburb { font-weight: 800; font-size: 16px; line-height: 1.15; }
  .clinic-phone { font-weight: 700; font-size: 15px; line-height: 1.15; color: var(--navy); }
  .clinic-address { font-family: "Arimo", sans-serif; font-size: 12px; line-height: 1.3; }
  .suppliers {
    position: absolute; left: 22px; top: 1140px;
    display: flex; gap: 42px; align-items: center;
    font-family: "Open Sans", sans-serif; font-weight: 700;
    font-size: 13px; color: #1f3b1a;
  }
</style>
</head>
<body>
<div class="canvas">
  <article class="flyer">
    <svg class="flyer-shapes" width="566" height="1165" viewBox="0 0 566 1165" aria-hidden="true">
      <defs>
        <linearGradient id="blueBand" x1="0" y1="0" x2="1" y2="0">
          <stop offset="0" stop-color="#0c7fb0"/>
          <stop offset="1" stop-color="#1ab0dc"/>
        </linearGradient>
        <linearGradient id="greenBand" x1="0" y1="0" x2="1" y2="0">
          <stop offset="0" stop-color="#3f9a2a"/>
          <stop offset="1" stop-color="#8cc63f"/>
        </linearGradient>
        <linearGradient id="greenPanel" x1="0" y1="0" x2="0" y2="1">
          <stop offset="0" stop-color="#8cc63f"/>
          <stop offset="1" stop-color="#3f9a2a"/>
        </linearGradient>
      </defs>
      <path class="top-wave" d="M0 500 C150 470 330 410 566 368 L566 470 C380 460 180 480 0 540 Z" fill="url(#blueBand)"/>
      <path class="top-wave-edge" d="M0 540 C180 480 380 460 566 470 L566 1165 L0 1165 Z" fill="#ffffff"/>
      <path class="offer-panel" d="M326 500 Q326 484 342 484 C420 490 480 470 536 464 L536 816 Q536 846 506 846 L356 846 Q326 846 326 816 Z" fill="url(#greenPanel)"/>
      <path class="bottom-wave" d="M0 1036 C170 1058 380 1048 566 995 L566 1165 L0 1165 Z" fill="url(#greenBand)"/>
      <path class="bottom-wave-line" d="M0 1036 C170 1058 380 1048 566 995" fill="none" stroke="#ffffff" stroke-width="5"/>
    </svg>

    <h1 class="brand-name">TAVRINCARE</h1>

    <div class="hero-machine" role="img" aria-label="Photo of a Talvix CPAP machine with its humidifier tub"></div>

    <section class="about">
      <h2 class="about-title">ABOUT US</h2>
      <p class="about-tagline">Proudly Independent!</p>
      <p class="about-body">Many CPAP clinics in Victoria are now owned by one or other of the big CPAP manufacturers; while many others only stock one brand. We stock all the leading brands and offer genuinely independent advice and friendly service.</p>
    </section>

    <div class="trial-offer">
      <p class="trial-price">$99</p>
      <p class="trial-label">CPAP<br>TRIAL</p>
      <p class="trial-details">Our all inclusive 4 week CPAP or APAP trial includes everything you need to get started for just $99. Plus we'll refund your trial fee when you're ready to buy your own machine.</p>
    </div>

    <div class="refund-note">
      <p class="refund-lead">Refundable</p>
      <p class="refund-main">trial fee</p>
      <p class="refund-tail">with purchase<br>of machine</p>
    </div>

    <div class="machine-inset" role="img" aria-label="Photo of an MDH CPAP machine on a bedside table"></div>

    <section class="contact">
      <h2 class="contact-title">Call us for an appointment</h2>
      <div class="clinics">
        <div class="clinic">
          <p class="clinic-suburb">Ashburton</p>
          <p class="clinic-phone">(03) 9412 6083</p>
          <p class="clinic-address">5/418 Dorran Street</p>
        </div>
        <div class="clinic">
          <p class="clinic-suburb">Brighton</p>
          <p class="clinic-phone">(03) 9263 5540</p>
          <p class="clinic-address">27b Tamsley Grove</p>
        </div>
        <div class="clinic">
          <p class="clinic-suburb">Kew East</p>
          <p class="clinic-phone">(03) 9351 2874</p>
          <p class="clinic-address">2637 Fennick Road</p>
        </div>
      </div>
    </section>

    <footer class="suppliers">
      <span class="supplier">CORVANE</span>
      <span class="supplier">Talvix</span>
      <span class="supplier">Morrow&amp;Dunlee</span>
    </footer>
  </article>
</div>
</body>
</html>
```